This book will apply the 12 Steps to gaming addiction, also known as video game addiction. The primary purpose of the book is to provide an effective solution for this new type of addiction. The solution is based on the rich and successful concepts of traditional twelve-step programs like RL.

The title on the cover will be "Nine Doors Past the Glowing Screen" and "by Martin Quorby". A subtitle can be used if it works in your design of "A Practical Path Beyond Compulsive Console Play". Cover will be for a 6" x 9" book approximately 110 pages in length.

Some back cover text including some review quotes and an author bio are in the attached Word doc. There is also an author photo attached for for the back cover.

Requirements
Must have
• For the cover design it could be stylized, or an image, a partial image, or whatever. I am open to suggestions. Think about what would be noticed by a person searching for help with moderating their video game use, or by the parents or loved ones of problem gamers. Something contemporary and eye catching.

```html
<!DOCTYPE html>
<html lang="en">
<head>
<meta charset="utf-8">
<title>Nine Doors Past the Glowing Screen — Martin Quorby</title>
<link rel="stylesheet" href="https://fonts.googleapis.com/css2?family=Chakra+Petch:wght@700&family=Montserrat:wght@400;500;600;800&display=swap">
<style>
  :root {
    --bg-deep: #070d11;
    --bg-mid: #0e1b22;
    --photo-light: #9cc4d2;
    --photo-glow: #3d6c7d;
    --photo-mid: #1d3944;
    --photo-dark: #0c181e;
    --ink-white: #f3f6f7;
    --ink-cyan: #43d9ec;
    --ink-cyan-dim: rgba(67, 217, 236, 0.35);
    --ink-soft: #e3ebee;
  }
  * { margin: 0; padding: 0; box-sizing: border-box; }
  html, body {
    width: 841px;
    height: 1200px;
    overflow: hidden;
    background: var(--bg-deep);
  }
  .cover {
    position: relative;
    width: 841px;
    height: 1200px;
    background: var(--bg-deep);
    overflow: hidden;
  }
  .cover-photo {
    position: absolute;
    inset: 0 0 auto 0;
    height: 760px;
    background:
      radial-gradient(ellipse 22% 9% at 50% 28%, rgba(156,196,210,0.55) 0%, rgba(156,196,210,0.15) 60%, transparent 100%),
      radial-gradient(ellipse 40% 22% at 50% 30%, var(--photo-glow) 0%, rgba(61,108,125,0.45) 50%, transparent 100%),
      radial-gradient(ellipse 70% 55% at 50% 38%, var(--photo-mid) 0%, rgba(29,57,68,0.6) 50%, transparent 100%),
      linear-gradient(180deg, #0a161c 0%, var(--photo-dark) 30%, #0f2029 55%, var(--bg-deep) 100%);
  }
  .cover-photo::after {
    content: "";
    position: absolute;
    inset: auto 0 0 0;
    height: 240px;
    background: linear-gradient(180deg, transparent, var(--bg-deep));
  }
  .title {
    font-weight: normal;
  }
  .title-lead {
    position: absolute;
    top: 572px;
    left: 0;
    right: 0;
    text-align: center;
    font-family: "Montserrat", sans-serif;
    font-weight: 500;
    font-size: 62px;
    line-height: 100px;
    color: var(--ink-white);
  }
  .title-lead .title-numeral {
    font-weight: 800;
    font-size: 100px;
    margin-right: 10px;
  }
  .title-main {
    position: absolute;
    top: 680px;
    left: 0;
    right: 0;
    text-align: center;
    font-family: "Chakra Petch", sans-serif;
    font-weight: 700;
    font-size: 104px;
    line-height: 96px;
    color: var(--ink-cyan);
    text-transform: uppercase;
    letter-spacing: 4px;
    text-shadow: -3px 0 var(--ink-cyan-dim), 3px 0 var(--ink-cyan-dim);
  }
  .subtitle {
    position: absolute;
    top: 1004px;
    left: 0;
    right: 0;
    text-align: center;
    font-family: "Montserrat", sans-serif;
    font-weight: 500;
    font-size: 21px;
    color: var(--ink-soft);
    text-transform: uppercase;
  }
  .author {
    position: absolute;
    top: 1084px;
    left: 0;
    right: 0;
    text-align: center;
    font-family: "Montserrat", sans-serif;
    font-weight: 400;
    font-size: 38px;
    color: var(--ink-white);
    text-transform: uppercase;
    letter-spacing: 8px;
  }
</style>
</head>
<body>
  <main class="cover">
    <div class="cover-photo" role="img" aria-label="Dark photograph of a seated person in a hoodie holding a wired game controller, face in shadow, lit in cool blue tones"></div>

    <h1 class="title">
      <span class="title-lead"><span class="title-numeral">Nine</span>Doors</span>
      <span class="title-main">Past the<br>Glowing<br>Screen</span>
    </h1>

    <p class="subtitle">A Practical Path Beyond Compulsive Console Play</p>

    <p class="author">Martin Quorby</p>
  </main>
</body>
</html>
```